Animated GIF banner for mobile app

We need a GIF Banner designed that alternates between two different ads.

Details are;
Pixel Size (W X H) 300 X 250
Minimum DPI 72dpi
File Size 40kb
File Size (Rich Media) 150kb

Ad 1 Text:
Lost super? More than one super fund? Contact us

Ad 2 Text:
Time to review your home loan? Contact us

Target Market(s)

30-55 year olds

Industry/Entity Type

Financial Service

Font styles to use
Sans Serif

Colors
0555a3
3176b5
85abd2

```html
<!DOCTYPE html>
<html lang="en">
<head>
<meta charset="utf-8">
<title>Super and Home Loan Banners</title>
<link href="https://fonts.googleapis.com/css2?family=Open+Sans:wght@400;700;800&display=swap" rel="stylesheet">
<style>
  :root {
    --page-bg: #ffffff;
    --navy-deep: #071a45;
    --navy-mid: #10306b;
    --navy-glow: #235797;
    --headline-top: #ffffff;
    --headline-bottom: #8fa6c4;
    --cta-yellow: #fdf7a6;
    --brand-blue: #0555a3;
    --brand-light: #85abd2;
    --frame-yellow: #f2e63a;
    --fold-light: #eef2f7;
    --fold-dark: #9fb0c4;
  }
  * { margin: 0; padding: 0; box-sizing: border-box; }
  html, body {
    width: 1200px; height: 1200px; overflow: hidden;
    background: var(--page-bg);
    font-family: "Open Sans", Arial, sans-serif;
  }
  .canvas { position: relative; width: 1200px; height: 1200px; }
  .banner {
    position: absolute; top: 400px; width: 480px; height: 400px; overflow: hidden;
    background:
      radial-gradient(ellipse 55% 45% at 75% 40%, rgba(49,118,181,0.55), transparent 70%),
      radial-gradient(ellipse 45% 40% at 25% 25%, rgba(60,100,160,0.45), transparent 70%),
      radial-gradient(ellipse 60% 50% at 50% 70%, rgba(35,87,151,0.45), transparent 75%),
      linear-gradient(180deg, var(--navy-mid), var(--navy-deep));
  }
  .banner--loan { left: 106px; }
  .banner--super { left: 615px; }
  .headline {
    position: absolute; left: 0; right: 0; text-align: center;
    font-weight: 700; font-size: 57px; line-height: 60px; letter-spacing: -0.5px;
    background: linear-gradient(180deg, var(--headline-top) 10%, var(--headline-bottom) 95%);
    -webkit-background-clip: text; background-clip: text; color: transparent;
    filter: drop-shadow(0 2px 3px rgba(0,0,0,0.6));
  }
  .banner--loan .headline { top: 46px; }
  .banner--super .headline { top: 26px; line-height: 63px; }
  .headline .line { display: block; }
  .banner--super .headline .line--gap { margin-bottom: 6px; }
  .cta {
    position: absolute; left: 0; right: 0; top: 234px; text-align: center;
    color: var(--cta-yellow); font-size: 37px; font-weight: 400;
  }
  .brand-box {
    position: absolute; left: 70px; top: 290px; width: 338px; height: 84px;
    background: #fff; border: 2px solid var(--frame-yellow);
    display: flex; align-items: center; gap: 16px; padding-left: 18px;
  }
  .brand-dot { width: 46px; height: 46px; border-radius: 50%; background: var(--brand-blue); flex: none; }
  .brand-name {
    color: var(--brand-blue); font-weight: 400; font-size: 26px; line-height: 28px;
  }
  .brand-name .sub { display: block; font-size: 18px; line-height: 22px; padding-left: 22px; }
  .page-curl { position: absolute; top: 0; right: 0; width: 56px; height: 56px; }
</style>
</head>
<body>
<div class="canvas">

  <section class="banner banner--loan">
    <h2 class="headline">
      <span class="line">Time to review</span>
      <span class="line">your home</span>
      <span class="line">loan?</span>
    </h2>
    <p class="cta">Contact us</p>
    <div class="brand-box">
      <span class="brand-dot"></span>
      <span class="brand-name">Daniel Hart<span class="sub">Financial Solutions</span></span>
    </div>
    <svg class="page-curl" viewBox="0 0 56 56" aria-hidden="true">
      <defs>
        <linearGradient id="foldA" x1="0" y1="0" x2="1" y2="1">
          <stop offset="0" stop-color="var(--fold-light)"/>
          <stop offset="1" stop-color="var(--fold-dark)"/>
        </linearGradient>
      </defs>
      <polygon points="0,0 56,0 56,56" fill="#ffffff"/>
      <path d="M0,0 Q6,40 56,56 L0,0 Z" fill="url(#foldA)"/>
      <path d="M0,0 Q6,40 56,56" fill="none" stroke="rgba(0,0,0,0.25)" stroke-width="1"/>
      <text x="8" y="22" font-size="7" fill="#6b7d94" font-family="Open Sans, sans-serif" transform="rotate(45 20 20)">Click me</text>
    </svg>
  </section>

  <section class="banner banner--super">
    <h2 class="headline">
      <span class="line line--gap">Lost super?</span>
      <span class="line">More than one</span>
      <span class="line">super fund?</span>
    </h2>
    <p class="cta">Contact us</p>
    <div class="brand-box">
      <span class="brand-dot"></span>
      <span class="brand-name">Daniel Hart<span class="sub">Financial Solutions</span></span>
    </div>
    <svg class="page-curl" viewBox="0 0 56 56" aria-hidden="true">
      <defs>
        <linearGradient id="foldB" x1="0" y1="0" x2="1" y2="1">
          <stop offset="0" stop-color="var(--fold-light)"/>
          <stop offset="1" stop-color="var(--fold-dark)"/>
        </linearGradient>
      </defs>
      <polygon points="0,0 56,0 56,56" fill="#ffffff"/>
      <path d="M0,0 Q6,40 56,56 L0,0 Z" fill="url(#foldB)"/>
      <path d="M0,0 Q6,40 56,56" fill="none" stroke="rgba(0,0,0,0.25)" stroke-width="1"/>
      <text x="8" y="22" font-size="7" fill="#6b7d94" font-family="Open Sans, sans-serif" transform="rotate(45 20 20)">Click me</text>
    </svg>
  </section>

</div>
</body>
</html>
```